VELK Website Redesign in Wix

Task:
Create a new design for all pages of the VELK technology website in Wix. Specifications are:
Color palette preferences: black, white, gray, purple, blue. See VELK Ref Doc provided.
Please refer to the VELK_ref doc for a sample of the desired color palette
Typesetting must be in Montserrat
Brand will be that of a Marketing Technology company
Looking for vibrant, highly engaging images and organized, digestible flow. Open to suggestions
Required format is Wix.
VELK logo does NOT need to be redesigned. Please use the files provided for the VELK logo.
Look and feel
Each slider illustrates characteristics of the customer's brand and the style your logo design should communicate.

```html
<!DOCTYPE html>
<html lang="en">
<head>
<meta charset="utf-8">
<title>VELK — Marketing Technology</title>
<link href="https://fonts.googleapis.com/css2?family=Montserrat:wght@400;500;600;700&family=Arimo:wght@400&display=swap" rel="stylesheet">
<style>
:root{
  --ink:#1a1a1a;
  --night:#040a1c;
  --deep:#0a1840;
  --purple:#8a12e6;
  --violet:#7a1fd6;
  --mist:#e9e9ec;
  --line:#b8b8be;
  --white:#ffffff;
  --muted:#3a3a3a;
  --partner:#5e5e5e;
}
*{margin:0;padding:0;box-sizing:border-box}
html,body{width:1200px;height:4255px;overflow:hidden;background:var(--white)}
body{font-family:"Montserrat",sans-serif;color:var(--ink);position:relative}
.abs{position:absolute}
.body-text{font-family:"Arimo",sans-serif;font-size:15px;line-height:27px;color:var(--muted);text-align:justify}
.accent-bar{position:absolute;left:111px;width:66px;height:8px;background:var(--purple)}
.section-title{position:absolute;left:111px;font-size:29px;font-weight:700;line-height:48px;letter-spacing:.3px;text-transform:uppercase;color:var(--ink)}

/* hero */
.hero{position:absolute;left:0;top:0;width:1200px;height:600px;
  background:
    radial-gradient(ellipse 380px 90px at 700px 470px,rgba(90,170,255,.55),rgba(90,170,255,0) 70%),
    radial-gradient(ellipse 300px 70px at 320px 430px,rgba(70,140,255,.45),rgba(70,140,255,0) 70%),
    radial-gradient(ellipse 260px 60px at 1000px 520px,rgba(60,130,240,.45),rgba(60,130,240,0) 70%),
    linear-gradient(172deg,rgba(0,0,0,0) 62%,rgba(40,110,230,.35) 72%,rgba(0,0,0,0) 82%),
    linear-gradient(180deg,#03081a 0%,#06112e 45%,#0c2460 78%,#0a1d4e 100%)}
.brand-mark{position:absolute;font-family:"Montserrat",sans-serif;font-weight:500;color:var(--white);letter-spacing:.22em}
.nav{position:absolute;top:32px;left:349px;font-family:"Arimo",sans-serif;font-size:15px;color:var(--white)}
.nav span{position:absolute;white-space:nowrap}
.login{position:absolute;left:992px;top:29px;display:flex;align-items:center;gap:10px;color:var(--white);font-family:"Arimo",sans-serif;font-size:15px}
.hero-sub{position:absolute;left:0;width:1200px;top:318px;text-align:center;color:#dfe6ff;font-family:"Arimo",sans-serif;font-size:15px;line-height:26px}
.hero-btn{position:absolute;left:526px;top:392px;width:148px;height:46px;background:var(--white);color:var(--purple);font-weight:600;font-size:16px;display:flex;align-items:center;justify-content:center}
.dots{position:absolute;left:1155px;top:198px}
.dot{position:absolute;left:0;width:14px;height:14px;border:2px solid var(--white);border-radius:50%}
.dot.on{background:var(--white)}
.dots-label{position:absolute;left:1099px;top:196px;color:var(--white);font-family:"Arimo",sans-serif;font-size:15px}

/* platform */
.platform{position:absolute;left:0;top:600px;width:1200px;height:480px;
  background:
    radial-gradient(ellipse 260px 200px at 820px 290px,rgba(150,162,182,.75),rgba(150,162,182,0) 75%),
    radial-gradient(ellipse 180px 120px at 1080px 180px,rgba(120,135,160,.5),rgba(120,135,160,0) 75%),
    linear-gradient(90deg,#e6e7eb 0%,#e1e3e9 42%,#d0d6df 68%,#b8c1cf 100%)}

/* grid */
.tile{position:absolute;width:400px;height:364px;display:flex;align-items:center;justify-content:center;text-align:center;color:var(--white);font-size:26px;font-weight:600;line-height:47px;text-transform:uppercase}
.tile .shade{position:absolute;inset:0}
.tile span{position:relative;text-shadow:0 1px 6px rgba(0,0,0,.35)}

/* partners */
.partner{position:absolute;color:var(--partner);white-space:nowrap}

/* team */
.team{position:absolute;left:0;top:2534px;width:1200px;height:375px;
  background:
    radial-gradient(ellipse 240px 190px at 980px 170px,rgba(140,152,172,.7),rgba(140,152,172,0) 75%),
    linear-gradient(90deg,#ebebec 0%,#ebebec 58%,#d3d7de 82%,#bcc4d0 100%)}
.portrait{position:absolute;top:2909px;width:300px;height:265px}
.portrait-label{position:absolute;left:0;width:300px;text-align:center;color:var(--white)}

/* contact */
.contact{position:absolute;left:0;top:3174px;width:1200px;height:839px;
  background:
    radial-gradient(ellipse 300px 260px at 1000px 500px,rgba(205,212,224,.6),rgba(205,212,224,0) 75%),
    linear-gradient(90deg,#fafafb 0%,#f4f5f7 55%,#e6e9ee 100%)}
.field-label{position:absolute;left:109px;font-family:"Arimo",sans-serif;font-size:14px;color:#333}
.field{position:absolute;left:111px;width:487px;height:60px;border:1.5px solid var(--line);background:var(--white);font-family:"Arimo",sans-serif;font-size:14px;color:#9a9a9a;padding:20px 18px}
.submit{position:absolute;left:450px;top:3893px;width:147px;height:44px;background:var(--purple);color:var(--white);font-weight:700;font-size:15px;display:flex;align-items:center;justify-content:center}
.contact-info{position:absolute;left:709px;font-size:17px;color:#222;font-weight:500}

/* footer */
.footer{position:absolute;left:0;top:4013px;width:1200px;height:242px;background:var(--ink)}
.social{position:absolute;top:4160px;width:20px;height:20px;border-radius:50%;background:var(--white)}
.chat{position:absolute;left:1026px;top:4128px;width:62px;height:61px;background:var(--purple);display:flex;align-items:center;justify-content:center}
</style>
</head>
<body>

<!-- hero -->
<section class="hero" role="img" aria-label="Glowing blue network of connected points and waves on a dark background"></section>
<div class="brand-mark" style="left:115px;top:14px;font-size:46px">VELK</div>
<nav class="nav">
  <span style="left:0">Home</span>
  <span style="left:76px">How it works</span>
  <span style="left:200px">VELK Applications</span>
  <span style="left:358px">Company</span>
  <span style="left:458px">Contact Us</span>
  <span style="left:568px">More</span>
</nav>
<div class="login">
  <svg width="26" height="26" viewBox="0 0 26 26"><circle cx="13" cy="13" r="12" fill="#fff"/><circle cx="13" cy="10" r="4.5" fill="#0a1840"/><path d="M5 21c2-4 5-5.5 8-5.5s6 1.5 8 5.5" fill="#0a1840"/></svg>
  <span>Log In</span>
</div>
<div class="brand-mark" style="left:0;width:1200px;text-align:center;top:188px;font-size:104px;letter-spacing:.2em;font-weight:600">VELK</div>
<p class="hero-sub">Increase and perfect your connection with consumers using VELK™'s<br>patented self-service content delivery technology</p>
<div class="hero-btn">LERN MORE</div>
<div class="dots-label">Home</div>
<div class="dots">
  <div class="dot on" style="top:0"></div>
  <div class="dot" style="top:37px"></div>
  <div class="dot" style="top:74px"></div>
  <div class="dot" style="top:111px"></div>
  <div class="dot" style="top:148px"></div>
  <div class="dot" style="top:185px"></div>
</div>

<!-- platform -->
<section class="platform" role="img" aria-label="Hand holding a tablet with floating commerce and logistics icons"></section>
<div class="accent-bar" style="top:683px"></div>
<h2 class="section-title" style="top:697px">Our revolutionary<br>platform</h2>
<p class="body-text abs" style="left:111px;top:808px;width:489px">Whether you're marketing software, selling a product, or looking to close a deal – find out your target market and quickly modify your campaigns to reach consumers silently and securely. Our platform goes far beyond basic ad optimization to deliver individualized content that immediately increases engagement over any communication medium with embedded tones.</p>

<!-- strategy -->
<div class="accent-bar" style="top:1169px"></div>
<h2 class="section-title" style="top:1184px">Strategy towards<br>market dominance</h2>
<p class="abs" style="left:111px;top:1298px;font-family:'Arimo',sans-serif;font-size:14px;color:#222">SOFTWARE AS A SERVICE (SAAS) PLATFORM</p>

<div class="tile" style="left:0;top:1393px"><div class="shade" role="img" aria-label="Colleagues reviewing work at a laptop in an office" style="background:radial-gradient(ellipse 180px 140px at 280px 110px,rgba(190,170,140,.55),rgba(190,170,140,0) 75%),radial-gradient(ellipse 220px 120px at 200px 330px,rgba(210,212,214,.45),rgba(210,212,214,0) 75%),linear-gradient(135deg,#8d9299,#565d66 55%,#30353c)"></div><span>Corporate<br>subscriptions</span></div>
<div class="tile" style="left:400px;top:1393px"><div class="shade" role="img" aria-label="Woman with digital security graphics in purple tones" style="background:radial-gradient(ellipse 120px 90px at 200px 60px,rgba(200,150,255,.55),rgba(200,150,255,0) 75%),radial-gradient(ellipse 200px 110px at 200px 250px,rgba(80,10,170,.55),rgba(80,10,170,0) 75%),linear-gradient(160deg,#a042f4,#7d22e2 50%,#5c12ba)"></div><span>NFT security</span></div>
<div class="tile" style="left:800px;top:1393px"><div class="shade" role="img" aria-label="Business team meeting around a laptop" style="background:radial-gradient(ellipse 140px 120px at 250px 120px,rgba(210,190,170,.45),rgba(210,190,170,0) 75%),radial-gradient(ellipse 200px 100px at 220px 310px,rgba(230,232,236,.4),rgba(230,232,236,0) 75%),linear-gradient(135deg,#a2a8b0,#5f666f 55%,#353b43)"></div><span>Advertising<br>campaigns</span></div>
<div class="tile" style="left:0;top:1757px"><div class="shade" role="img" aria-label="Glowing circuit board with globe graphic" style="background:radial-gradient(ellipse 110px 90px at 240px 90px,rgba(90,180,255,.6),rgba(90,180,255,0) 75%),radial-gradient(ellipse 260px 120px at 180px 300px,rgba(40,120,210,.45),rgba(40,120,210,0) 75%),linear-gradient(180deg,#0b2240,#0a2a52 55%,#061426)"></div><span>Technology<br>licensing</span></div>
<div class="tile" style="left:400px;top:1757px"><div class="shade" role="img" aria-label="Businessman touching floating data charts" style="background:radial-gradient(ellipse 140px 120px at 100px 130px,rgba(200,210,225,.45),rgba(200,210,225,0) 75%),radial-gradient(ellipse 160px 160px at 320px 170px,rgba(80,130,200,.55),rgba(80,130,200,0) 75%),linear-gradient(135deg,#3a4250,#2c3c5e 55%,#3c5a8a)"></div><span>Platform<br>integrations</span></div>
<div class="tile" style="left:800px;top:1757px"><div class="shade" role="img" aria-label="Worker walking through a warehouse aisle" style="background:radial-gradient(ellipse 80px 160px at 200px 180px,rgba(230,230,225,.45),rgba(230,230,225,0) 75%),linear-gradient(90deg,rgba(160,90,50,.45),rgba(0,0,0,0) 30%,rgba(0,0,0,0) 70%,rgba(160,90,50,.45)),linear-gradient(180deg,#5a7294,#3d5270 50%,#5e4b38)"></div><span>Ad tech<br>licensing</span></div>

<!-- partners -->
<div class="accent-bar" style="top:2210px"></div>
<h2 class="section-title" style="top:2226px">Our customers and<br>partners</h2>
<div class="partner" style="left:114px;top:2384px;font-size:34px;font-weight:600">Corvane</div>
<div class="partner" style="left:416px;top:2390px;font-size:28px;font-weight:600">Northmark</div>
<div class="partner" style="left:700px;top:2388px;font-size:28px;font-weight:600">Linden Fair</div>
<div class="partner" style="left:899px;top:2412px;font-size:15px;font-weight:500;letter-spacing:.15em">OSRIC &amp; PELL</div>

<!-- team -->
<section class="team" role="img" aria-label="Business person holding a tablet"></section>
<div class="accent-bar" style="top:2620px"></div>
<h2 class="section-title" style="top:2631px">Our<br>team</h2>
<p class="body-text abs" style="left:111px;top:2743px;width:489px">Lorem ipsum dolor sit amet, consectetur adipiscing elit, sed do eiusmod tempor incididunt ut labore et dolore magna aliqua. Ut enim ad minim veniam, quis nostrud exercitation ullamco laboris nisi ut aliquip ex ea commodo consequat.</p>

<div class="portrait" role="img" aria-label="Portrait of the founder and CEO" style="left:0;background:radial-gradient(ellipse 130px 110px at 150px 150px,rgba(150,90,235,.6),rgba(150,90,235,0) 75%),linear-gradient(180deg,#7a24d8,#5f16b8)">
  <div class="portrait-label" style="top:106px;font-size:22px;font-weight:700">Marcus L. Hayden</div>
  <div class="portrait-label" style="top:136px;font-size:17px;font-weight:500">Founder,CEO</div>
</div>
<div class="portrait" role="img" aria-label="Portrait of a smiling team member" style="left:300px;background:radial-gradient(ellipse 110px 140px at 150px 200px,rgba(25,28,34,.7),rgba(25,28,34,0) 75%),#364552"></div>
<div class="portrait" role="img" aria-label="Portrait of a team member in a suit" style="left:600px;background:radial-gradient(ellipse 110px 140px at 150px 210px,rgba(40,48,70,.75),rgba(40,48,70,0) 75%),#a7a7a9"></div>
<div class="portrait" role="img" aria-label="Portrait of a team member in a blazer" style="left:900px;background:radial-gradient(ellipse 110px 140px at 150px 210px,rgba(25,30,40,.7),rgba(25,30,40,0) 75%),#364552"></div>

<!-- contact -->
<section class="contact" role="img" aria-label="Faded office desk with documents in the background"></section>
<div class="accent-bar" style="top:3251px"></div>
<h2 class="section-title" style="top:3261px">What can we help<br>you with?</h2>
<div class="field-label" style="top:3406px">Enter Your Name *</div>
<div class="field" style="top:3438px">Name</div>
<div class="field-label" style="top:3510px">Enter Your Email *</div>
<div class="field" style="top:3541px">Email</div>
<div class="field-label" style="top:3612px">Enter Your Subject *</div>
<div class="field" style="top:3643px">Subject</div>
<div class="field-label" style="top:3714px">Enter Your Message *</div>
<div class="field" style="top:3746px;height:129px">Message</div>
<div class="submit">SUBMIT</div>
<div class="contact-info" style="top:3426px;font-size:21px">We can't wait to hear from you</div>
<div class="contact-info" style="top:3517px">info@velktech.com</div>
<div class="contact-info" style="top:3576px">1-866-TRY-VELK</div>
<div class="contact-info" style="top:3632px;line-height:28px">Lorem ipsum dolor sit amet,<br>consectetur</div>

<!-- footer -->
<footer class="footer"></footer>
<div class="brand-mark" style="left:110px;top:4098px;font-size:64px;font-weight:600;letter-spacing:.2em">VELK</div>
<div class="abs" style="left:483px;top:4096px;color:var(--white);font-weight:600;font-size:18px">Be a SociaLight and &nbsp;Follow Us:</div>
<div class="social" style="left:481px"></div>
<div class="social" style="left:525px"></div>
<div class="social" style="left:574px"></div>
<div class="social" style="left:622px"></div>
<div class="chat">
  <svg width="32" height="30" viewBox="0 0 32 30"><path d="M3 3h26v18H12l-7 6v-6H3z" fill="none" stroke="#fff" stroke-width="2.5" stroke-linejoin="round"/><path d="M9 10h14M9 15h10" stroke="#fff" stroke-width="2.5"/></svg>
</div>
<div class="abs" style="left:0;width:1200px;top:4224px;text-align:center;color:var(--white);font-family:'Arimo',sans-serif;font-size:14px">©Copyrights 2022 velktech &nbsp; | &nbsp; All Rights Reserved</div>

</body>
</html>
```